Banner Ad Design Project

It is a banner for an email. It must fit the standard email width. The height should be more than a standard banner, but the majority of the banner should appear above the email screen "fold" when someone opens their email.

Target Market(s)

Oral surgeons

Requirements
Must have
• Must include 3 dental implant images which is our main product focus. The main part of the banner add should include four circles which intersect at a common point. Each circle should contain (should be written in the circle) one of the four following principles "Support - When and how you need it", "Value - Quality at a fair price", "Made in the USA" "Compatible with major implant systems" The idea is that the company sits at the intersection of these circles / principles.
Please see our website homepage www.fernwickdent.com for the general colors and design style.
Next to the image "one stage.tif" it should say "Kelvorth Compatible" and "$95"
Next to the image "internal hex.tif" it should say "Pradlo Compatible" and "$117"
Next to the image "trilobe.tif" it should say "Tavik Compatible" and "$145"

```html
<!DOCTYPE html>
<html lang="en">
<head>
<meta charset="utf-8">
<title>Implant Banner</title>
<link href="https://fonts.googleapis.com/css2?family=Arimo:wght@400;700&display=swap" rel="stylesheet">
<style>
  :root {
    --bg-pink: #f6d9ec;
    --bg-lilac: #d9c6f2;
    --bg-blue: #a9c4f0;
    --bg-violet: #b39be8;
    --label-grey: #8d92b4;
    --price-pink: #e2679a;
    --circle-text: #27357a;
    --implant-light: #e4e6ee;
    --implant-mid: #b8bccb;
  }
  html, body {
    margin: 0;
    padding: 0;
    overflow: hidden;
  }
  body {
    width: 1200px;
    height: 327px;
    font-family: "Arimo", Arial, sans-serif;
  }
  .banner {
    position: relative;
    width: 1200px;
    height: 327px;
    overflow: hidden;
    background:
      radial-gradient(ellipse 420px 260px at 140px 120px, rgba(255,240,250,0.9), transparent 70%),
      radial-gradient(ellipse 380px 260px at 1150px 60px, var(--bg-violet), transparent 70%),
      linear-gradient(100deg, var(--bg-pink) 0%, var(--bg-lilac) 40%, var(--bg-blue) 75%, var(--bg-violet) 100%);
  }
  .product-image {
    position: absolute;
    left: 78px;
    top: 57px;
    width: 100px;
    height: 172px;
    border-radius: 12px 12px 36px 36px;
    background: linear-gradient(90deg, var(--implant-mid), var(--implant-light) 45%, var(--implant-mid));
    opacity: 0.75;
  }
  .product-info {
    position: absolute;
    left: 164px;
    top: 63px;
    color: var(--label-grey);
  }
  .product-name {
    font-size: 23px;
    font-weight: 700;
    margin: 0;
  }
  .product-compat {
    font-size: 18px;
    font-weight: 700;
    line-height: 26px;
    margin: 2px 0 0 4px;
    opacity: 0.8;
  }
  .product-price {
    position: absolute;
    left: 220px;
    top: 160px;
    font-size: 64px;
    font-weight: 700;
    color: var(--price-pink);
    text-shadow: 0 0 2px #fff, 0 0 6px rgba(255,255,255,0.8);
    margin: 0;
  }
  .principles {
    position: absolute;
    inset: 0;
  }
  .principle-label {
    position: absolute;
    transform: translate(-50%, -50%);
    text-align: center;
    color: var(--circle-text);
    font-size: 22px;
    line-height: 27px;
    margin: 0;
    white-space: nowrap;
  }
  .principle-label strong { font-weight: 700; }
</style>
</head>
<body>
<div class="banner">
  <div class="product-image" role="img" aria-label="Internal hex dental implant"></div>
  <div class="product-info">
    <p class="product-name">Fernwick Internal Hex</p>
    <p class="product-compat">Pradlo<br>Compatible</p>
  </div>
  <p class="product-price">$117</p>

  <svg class="principles" width="1200" height="327" viewBox="0 0 1200 327" aria-hidden="true">
    <defs>
      <radialGradient id="bubble" cx="50%" cy="45%" r="55%">
        <stop offset="0%" stop-color="#ffffff" stop-opacity="0.05"/>
        <stop offset="80%" stop-color="#ffffff" stop-opacity="0.18"/>
        <stop offset="100%" stop-color="#ffffff" stop-opacity="0.4"/>
      </radialGradient>
    </defs>
    <g fill="url(#bubble)" stroke="#ffffff" stroke-opacity="0.85" stroke-width="3">
      <circle cx="619" cy="106" r="105"/>
      <circle cx="839" cy="220" r="140"/>
      <circle cx="1073" cy="158" r="126"/>
      <circle cx="1045" cy="376" r="180"/>
    </g>
  </svg>

  <p class="principle-label" style="left:619px; top:122px;">Support -&nbsp; When<br>and how you<br>need it</p>
  <p class="principle-label" style="left:839px; top:216px;">Compatible with<br>major implant<br>systems</p>
  <p class="principle-label" style="left:1073px; top:137px;">Value - Quality<br>at a fair price</p>
  <p class="principle-label" style="left:1048px; top:278px;">Made in the<br><strong>USA</strong></p>
</div>
</body>
</html>
```